Wordpress Design Project

We need a Web page. That runs under wordpress. We have a domain- www.lomavrenta.us

The page shall consist of five buttons- home, about, services, projects, contact.

My current clients are-

Bright quarry electronics, inc.
Pelwinter coffee
Vantrocket
Lease a Corner
Grolf
Top penny depot
Quillans Steakhouse
RKVELO

Incorporate customer logos in my website

Our services include:

-Fire alarm systems
-Fire alarm system design

-Security
-Card Access
-CCTV/IP Cameras

-Communication systems
-Intercom/entry phone
-Nurse call systems

The page needs to be simple and professional.

The site needs to be loaded on word press and fully functional.
I also need to have the ability to make small edits later on, or when we add clients to add to the list.
Updates

Target Market(s)

Target market is- electrical contractors, end customers

Industry/Entity Type

Electronics

Requirements
Must have
• Partners-
http://www.structuresolutions.dravenko.com/bt/global/en/firesafety/fire-safety-products/Pages/fire-safety-products.aspx

http://www.dravenko.com/entry/cc/en/
http://www.kolbrisk.com/
http://www.mistyharbor.com/
Plaxtondale
Voribel

```html
<!DOCTYPE html>
<html lang="en">
<head>
<meta charset="utf-8">
<title>LMV Fire and Security</title>
<link href="https://fonts.googleapis.com/css2?family=Arimo:wght@400;700&display=swap" rel="stylesheet">
<style>
:root{
  --page:#efefef;
  --panel:#ffffff;
  --header-top:#f4f4f4;
  --header-bottom:#dcdcdc;
  --nav:#3b3e40;
  --nav-text:#e8e8e8;
  --text:#333333;
  --muted:#777777;
  --line:#dcdcdc;
  --orange:#f39a1e;
  --blue:#3aa0cf;
  --green:#9cc23c;
  --logo-orange:#e8731e;
  --hero-top:#e9e9e9;
  --hero-bottom:#c9c9c9;
}
*{box-sizing:border-box;margin:0;padding:0}
html,body{width:1200px;height:900px;overflow:hidden}
body{background:var(--page);font-family:"Arimo",Arial,sans-serif;color:var(--text);position:relative}
.site{position:absolute;left:206px;top:0;width:790px;height:680px;background:var(--panel);border-radius:0 0 10px 10px;box-shadow:0 1px 4px rgba(0,0,0,.12);overflow:hidden}
.masthead{height:80px;background:linear-gradient(var(--header-top),var(--header-bottom));position:relative}
.brand{position:absolute;left:14px;top:14px;display:flex;align-items:center;gap:10px}
.brand-mark{width:36px;height:36px;border-radius:50%;background:var(--logo-orange)}
.brand-name{font-weight:700;font-size:34px;line-height:30px;color:#555;letter-spacing:1px}
.brand-tag{font-size:12px;color:#555;font-weight:700}
.search{position:absolute;left:638px;top:40px;width:150px;height:22px;border:1px solid #c8c8c8;border-radius:3px;background:#fff;font-size:10px;color:#666;padding:5px 6px;display:flex;justify-content:space-between;align-items:center}
.main-nav{height:26px;background:var(--nav);display:flex;padding-left:14px}
.main-nav a{color:var(--nav-text);text-decoration:none;font-size:13px;line-height:26px;padding:0 12px;position:relative}
.main-nav a.active{background:#fff;color:#333;margin-top:2px;line-height:24px}
.main-nav a.active::after{content:"";display:inline-block;width:7px;height:7px;border-radius:50%;background:var(--green);margin-left:5px}
.dropdown{position:absolute;left:76px;top:106px;width:114px;background:#fff;box-shadow:0 2px 4px rgba(0,0,0,.2);z-index:3}
.dropdown a{display:block;font-size:10px;color:#333;padding:7px 10px;border-bottom:1px solid #e6e6e6;text-decoration:none}
.hero{height:294px;background:linear-gradient(var(--hero-top),var(--hero-bottom));position:relative}
.hero-photo{position:absolute;left:24px;top:18px;width:454px;height:248px;background:linear-gradient(110deg,#8d9aa6 0%,#cfd5da 45%,#f1f1f1 80%)}
.hero-copy{position:absolute;left:494px;top:36px;width:250px}
.hero-copy h1{font-weight:400;font-size:24px;color:#333;margin-bottom:10px}
.hero-copy p{font-size:10px;line-height:14px;color:#555;margin-bottom:14px}
.btn{display:inline-block;font-size:8px;color:#fff;padding:3px 6px;text-transform:uppercase;margin-right:4px}
.btn-orange{background:var(--orange)}
.btn-blue{background:var(--blue)}
.btn-green{background:var(--green)}
.section-label{position:absolute;left:26px;top:400px;font-size:10px;color:var(--orange)}
.services{position:absolute;left:14px;top:410px;width:762px;height:142px;border:1px solid var(--line);border-radius:4px;display:flex;background:#fff}
.service{flex:1;padding:10px 12px;border-right:1px solid var(--line);position:relative}
.service:last-child{border-right:0}
.service h2{font-weight:400;font-size:17px;margin-bottom:10px}
.service-body{display:flex;gap:10px}
.service-body svg{flex:none}
.service-body p{font-size:10px;line-height:13px;color:#555}
.service .btn{position:absolute;left:56px;top:106px}
.features{position:absolute;left:26px;top:566px;width:460px}
.features .kicker{font-size:11px;color:#555}
.features h2{font-weight:400;font-size:24px;margin:6px 0 8px}
.features p{font-size:10px;line-height:14px;color:#555}
.pager{display:flex;gap:4px;align-items:center;margin-top:10px}
.pager span{width:7px;height:7px;border-radius:50%;background:#bbb}
.pager span.on{background:#555}
.pager em{font-style:normal;font-size:7px;border:1px solid #bbb;padding:0 3px;color:#666}
.clients{position:absolute;left:206px;top:704px;width:790px;height:116px;background:#fff;border-radius:6px 6px 50% 50%/6px 6px 30px 30px;box-shadow:0 1px 4px rgba(0,0,0,.12)}
.clients h3{font-weight:400;font-size:12px;color:#555;position:absolute;left:26px;top:12px}
.client-row{position:absolute;left:10px;right:10px;top:32px;height:64px;display:flex;justify-content:space-around;align-items:center}
.client{display:flex;align-items:center;gap:6px;font-size:18px;color:#5b6aa8}
.client-dot{width:20px;height:20px;border-radius:50%;background:#5b6aa8}
.footer{position:absolute;left:0;width:1200px;top:856px;text-align:center;font-size:10px;line-height:13px;color:#888}
</style>
</head>
<body>
<div class="site">
  <header class="masthead">
    <div class="brand">
      <span class="brand-mark"></span>
      <div><div class="brand-name">LMV</div><div class="brand-tag">Fire and Security</div></div>
    </div>
    <div class="search"><span>Search</span>
      <svg width="10" height="10" viewBox="0 0 10 10"><circle cx="4" cy="4" r="3" fill="none" stroke="#777" stroke-width="1.5"/><line x1="6" y1="6" x2="9" y2="9" stroke="#777" stroke-width="1.5"/></svg>
    </div>
  </header>
  <nav class="main-nav">
    <a href="#">Home</a><a href="#" class="active">About</a><a href="#">Projects</a><a href="#">Contact</a>
  </nav>
  <div class="dropdown"><a href="#">Our team</a><a href="#">Customers</a><a href="#">Vacancies</a></div>
  <section class="hero">
    <div class="hero-photo" role="img" aria-label="Photo of a technician on the phone in a server room"></div>
    <div class="hero-copy">
      <h1>Catchy Header</h1>
      <p>Lorem ipsum dolor sit amet consectetur adipiscing elit nunc ullamcorper blandit urna. Sed facilisis accumsan nisi. Ut mattis libero quis sapien. Integer fermentum venenatis tortor.</p>
      <span class="btn btn-orange">Order project</span><span class="btn btn-blue">View details</span>
    </div>
  </section>
  <div class="section-label">Services</div>
  <section class="services">
    <article class="service">
      <h2>Fire Alarm Systems</h2>
      <div class="service-body">
        <svg width="34" height="34" viewBox="0 0 34 34"><rect x="2" y="4" width="30" height="26" fill="none" stroke="#999" stroke-width="2"/><line x1="2" y1="10" x2="32" y2="10" stroke="#999" stroke-width="2"/><rect x="6" y="14" width="9" height="12" fill="#bbb"/><line x1="18" y1="16" x2="28" y2="16" stroke="#bbb" stroke-width="2"/><line x1="18" y1="21" x2="28" y2="21" stroke="#bbb" stroke-width="2"/></svg>
        <p>Lorem ipsum dolor sit amet consectetur adipiscing elit nunc ullamcorper blandit urna. Sed facilisis accumsan nisi. Ut mattis libero quis</p>
      </div>
      <span class="btn btn-green">Read more</span>
    </article>
    <article class="service">
      <h2>Security Systems</h2>
      <div class="service-body">
        <svg width="34" height="34" viewBox="0 0 34 34"><circle cx="13" cy="15" r="8" fill="none" stroke="#999" stroke-width="5" stroke-dasharray="4 2.3"/><circle cx="13" cy="15" r="3" fill="#999"/><circle cx="26" cy="26" r="4" fill="none" stroke="#aaa" stroke-width="3" stroke-dasharray="2.5 1.6"/></svg>
        <p>Lorem ipsum dolor sit amet consectetur adipiscing elit nunc ullamcorper blandit urna. Sed facilisis accumsan nisi. Ut mattis libero quis</p>
      </div>
      <span class="btn btn-green">Read more</span>
    </article>
    <article class="service">
      <h2>Communication Systems</h2>
      <div class="service-body">
        <svg width="34" height="34" viewBox="0 0 34 34"><rect x="4" y="22" width="5" height="8" fill="#aaa"/><rect x="11" y="17" width="5" height="13" fill="#aaa"/><rect x="18" y="12" width="5" height="18" fill="#aaa"/><rect x="25" y="7" width="5" height="23" fill="#aaa"/><polyline points="3,16 13,9 20,11 31,3" fill="none" stroke="#888" stroke-width="2"/></svg>
        <p>Lorem ipsum dolor sit amet consectetur adipiscing elit nunc ullamcorper blandit urna. Sed facilisis accumsan nisi. Ut mattis libero quis</p>
      </div>
      <span class="btn btn-green">Read more</span>
    </article>
  </section>
  <section class="features">
    <div class="kicker">Features</div>
    <h2>Space for a feature</h2>
    <p>Etiam dignissim lectus id diam varius egestas. Curabitur vel libero massa. Phasellus scelerisque est ac enim interdum pharetra. Nam tristique venenatis tortor non interdum.</p>
    <div class="pager"><span></span><span class="on"></span><span></span><span></span><span></span><em>NEXT</em></div>
  </section>
</div>
<section class="clients">
  <h3>Our Clients</h3>
  <div class="client-row">
    <div class="client"><span class="client-dot"></span>Lease a Corner</div>
    <div class="client">Grolf</div>
    <div class="client">Quillans Steakhouse</div>
    <div class="client">Vantrocket</div>
    <div class="client">Pelwinter coffee</div>
  </div>
</section>
<footer class="footer">Copyright 2011 LMV Fire and Security<br>All Rights Reserved</footer>
</body>
</html>
```